Nine Lanterns Quill House Book Cover for: "Growing Older Wisely"

We are a publishing company who plans to launch the book, Growing Older Wisely, A Handy Compact Manual for Legal, Financial and Emotional Health in late 2018. We desire a book cover that creates interest, looks professional and can draw readers to open and purchase this book. Growing Older Wisely is an invaluable, self-help book which provides Generation X, Baby Boomers and their families with the following information: steps to obtain valid, reliable wills and trusts, identify and pay for health care, address end of life care and manage grief. (Please see the attached book description for more information about the book contents). The cover needs to have a "wellness", health and healing emphasis but it should not be morbid. Instead, the cover should have an uplifting, inviting and engaging feeling.

The designer should use Photoshop to develop the 5 x 7 cover. Please design the front, back cover and spine using the attached suggested layout as a guide. Use colors that complement the background colors in the author's photo and the logo for the front and back colors. Feel free to change the colors of the black rectangles on the front of the book. We are looking for a design to be added using the suggested layouts but we are open to modifications of the layout provided that all the content in the attachments are used. Below are the specifications needed for the cover:

-Use Photoshop
-Develop a front and back cover for a 5 x 7 format book
-Include the book title, subtitle and author name on the front cover as noted on the front cover attachment
-Include a book title and author names on the spine of the cover
-Use full bleed background if appropriate
-Color correct and resize images as necessary
-Insert logo and publisher’s imprint on spine and back cover as noted in attachments

For designers who are successful with this contest, we will primarily consider you for future projects.

Thanks!

Target Market(s)

Generation X, Baby Boomers and their families

Industry/Entity Type

Book Publisher

Font styles to use
Sans Serif

Colors

Designer to choose colors to be used in the design.

Requirements
Must have
• The designer should use Photoshop to develop the 5 x 7 cover. Please design the front, back cover and spine using the attached suggested layout as a guide. Use colors that complement the background colors in the author's photo and the logo for the front and back colors. Feel free to change the colors of the black rectangles on the front of the book. We are looking for a design to be added using the suggested layouts but we are open to modifications of the layout provided that all the content in the attachments are used. Below are the specifications needed for the cover:
• -Use Photoshop
• -Develop a front and back cover for a 5 x 7 format book
• -Include the book title, subtitle and author name on the front cover as noted on the front cover attachment
• -Include a book title and author names on the spine of the cover
• -Use full bleed background if appropriate
• -Color correct and resize images as necessary
• -Insert logo and publisher’s imprint on spine and back cover as noted in attachments
Nice to have
• N/A
Should not have
• The design should not specifically duplicate the layout samples or include pictures of persons on the cover. We have provided those as a guide; we are looking for innovation and professionalism.

```html
<!DOCTYPE html>
<html lang="en">
<head>
<meta charset="utf-8">
<title>Growing Older Wisely — Book Cover</title>
<link rel="stylesheet" href="https://fonts.googleapis.com/css2?family=Noto+Serif:wght@400&family=Marcellus+SC&family=Fira+Sans+Condensed:ital,wght@0,600;1,400&display=swap">
<style>
  :root {
    --stage: #e6e6e6;
    --navy: #2a2f86;
    --red: #d41f2a;
    --paper: #f1f1f2;
    --paper-shade: #e3e4e6;
    --white: #ffffff;
    --ink: #1e1e24;
  }
  * { margin: 0; padding: 0; box-sizing: border-box; }
  html, body { width: 1200px; height: 819px; overflow: hidden; background: var(--stage); }
  .canvas { position: relative; width: 1200px; height: 819px; }

  .book { position: absolute; left: 315px; top: 60px; width: 570px; height: 700px; display: flex; box-shadow: 0 14px 30px rgba(0,0,0,.18); }

  /* Spine */
  .spine { position: relative; width: 70px; height: 100%; background: var(--paper); border-right: 1px solid #cfd0d4; }
  .spine__top { position: absolute; top: 0; left: 0; right: 0; height: 140px; background: var(--navy); display: flex; justify-content: center; padding-top: 22px; }
  .spine__authors { writing-mode: vertical-rl; font-family: "Marcellus SC", serif; font-size: 9px; color: var(--white); line-height: 1.35; }
  .spine__rule { position: absolute; left: 0; right: 0; height: 8px; background: var(--red); }
  .spine__rule--top { top: 140px; }
  .spine__rule--bottom { top: 540px; height: 14px; }
  .spine__middle { position: absolute; top: 160px; left: 0; right: 0; height: 370px; display: flex; flex-direction: row-reverse; justify-content: center; gap: 4px; }
  .spine__title { writing-mode: vertical-rl; font-family: "Noto Serif", serif; font-size: 25px; color: var(--red); }
  .spine__subtitle { writing-mode: vertical-rl; font-family: "Marcellus SC", serif; font-size: 9px; color: var(--ink); padding-top: 2px; }
  .spine__publisher { position: absolute; top: 570px; left: 0; right: 0; bottom: 16px; display: flex; flex-direction: column; align-items: center; gap: 8px; }
  .spine__mark { width: 14px; height: 14px; background: var(--navy); }
  .spine__imprint { writing-mode: vertical-rl; font-family: "Fira Sans Condensed", sans-serif; font-weight: 600; font-size: 10px; color: var(--ink); }

  /* Front cover */
  .front { position: relative; width: 500px; height: 100%; background: var(--paper); overflow: hidden; }
  .front__band { position: absolute; top: 0; left: 0; right: 0; height: 140px; background: var(--navy); }
  .praise { position: absolute; top: 60px; left: 0; right: 0; text-align: center; font-family: "Fira Sans Condensed", sans-serif; font-style: italic; }
  .praise__quote { display: block; font-size: 34px; color: var(--red); line-height: 1; }
  .praise__source { display: block; font-size: 12px; color: var(--white); margin-left: 130px; margin-top: 2px; }
  .front__rule { position: absolute; left: 0; right: 0; height: 8px; background: var(--red); }
  .front__rule--top { top: 140px; }
  .front__rule--bottom { top: 548px; height: 10px; }
  .front__photo { position: absolute; top: 148px; left: 0; right: 0; height: 400px;
    background: linear-gradient(90deg, #e9c7b3 0%, #f0d2c2 35%, #e8c6b2 60%, #d9b7a4 80%, #c9ccd3 100%); }
  .title { position: absolute; top: 340px; left: 0; right: 0; text-align: center; font-family: "Noto Serif", serif; font-size: 48px; color: var(--red);
    -webkit-text-stroke: 1px var(--white); paint-order: stroke fill; text-shadow: 0 0 3px var(--white), 0 0 6px rgba(255,255,255,.8); }
  .subtitle { position: absolute; top: 590px; left: 0; right: 0; text-align: center; font-family: "Marcellus SC", serif; font-size: 18px; line-height: 1.35; color: var(--red); }
  .authors { position: absolute; top: 655px; left: 0; right: 0; text-align: center; font-family: "Marcellus SC", serif; font-size: 14px; color: var(--red); }
  .authors em { font-family: "Fira Sans Condensed", sans-serif; font-size: 12px; }
</style>
</head>
<body>
<main class="canvas">
  <div class="book">
    <aside class="spine">
      <div class="spine__top">
        <p class="spine__authors">Dana R. Ellison, M.P.A.<br>with Martin K. Hale, Esq.</p>
      </div>
      <div class="spine__rule spine__rule--top"></div>
      <div class="spine__middle">
        <h2 class="spine__title">Growing Older Wisely</h2>
        <p class="spine__subtitle">A Handy Compact Manual for Legal, Financial and Emotional Health</p>
      </div>
      <div class="spine__rule spine__rule--bottom"></div>
      <div class="spine__publisher">
        <span class="spine__mark"></span>
        <span class="spine__imprint">Nine Lanterns Quill House</span>
      </div>
    </aside>

    <section class="front">
      <div class="front__band"></div>
      <p class="praise">
        <span class="praise__quote">“Indispensable!”</span>
        <span class="praise__source">The Riverbend Ledger</span>
      </p>
      <div class="front__rule front__rule--top"></div>
      <div class="front__photo" role="img" aria-label="Photograph of three overlapping portraits showing a woman's face at progressively older ages"></div>
      <h1 class="title">Growing Older Wisely</h1>
      <div class="front__rule front__rule--bottom"></div>
      <p class="subtitle">A Handy Compact Manual<br>for Legal, Financial and Emotional Health</p>
      <p class="authors">Dana R. Ellison, M.P.A. <em>with</em> Martin K. Hale, Esq.</p>
    </section>
  </div>
</main>
</body>
</html>
```